Tarvell homes and renovations business card design.

Would like some new card designs utilizing my new logo that look professional. I am open to different colors on the logo or utilize the same ones we have. I like the original concept but would like to see some fresh ideas and build on what we have already done.

Target Market(s)

Custom home building industry, Real estate sales, Renovation projects.

Industry/Entity Type

Home Builder

Contact Information for Business Card

Tarvell Homes and Renovations
2871 162nd Street
Brennick, Northshire
T0L3P0
Home : 403- 555-0187 Cell: 403- 555-0243

My info is : Gus Tarvell, President and CEO
email: tarvellhomes@quillmail.example
Website: tarvellhomes.example

Requirements
Must have
• Must Use my new logo design. I am open to different colors on the logo or utilize the same ones in the existing design. I can upload the original logo design if needed.

```html
<!DOCTYPE html>
<html lang="en">
<head>
<meta charset="utf-8">
<title>Tarvell Homes and Renovations – Business Card</title>
<link href="https://fonts.googleapis.com/css2?family=Source+Sans+3:wght@400;600;700&display=swap" rel="stylesheet">
<style>
  :root {
    --page-bg: #ecebe8;
    --card-white: #ffffff;
    --brand-yellow: #f9bd1f;
    --brand-bronze: #b48535;
    --ink: #1f1a12;
    --font-main: "Source Sans 3", "Myriad Pro", Arial, sans-serif;
  }
  html, body {
    margin: 0;
    width: 1200px;
    height: 900px;
    overflow: hidden;
    background: var(--page-bg);
    font-family: var(--font-main);
  }
  .business-card {
    position: absolute;
    left: 97px;
    top: 139px;
    width: 1005px;
    height: 622px;
    background: var(--card-white);
    overflow: hidden;
    box-shadow: 0 10px 30px rgba(0,0,0,0.18);
  }
  .card-waves {
    position: absolute;
    inset: 0;
    width: 100%;
    height: 100%;
  }
  .brand-name {
    position: absolute;
    left: 0;
    right: 0;
    top: 172px;
    text-align: center;
    font-size: 50px;
    font-weight: 600;
    color: var(--brand-bronze);
    letter-spacing: 0.5px;
    margin: 0;
  }
  .holder-block {
    position: absolute;
    left: 50px;
    top: 352px;
    color: var(--ink);
  }
  .holder-name {
    margin: 0;
    font-size: 36px;
    font-weight: 600;
    line-height: 1.1;
  }
  .holder-title {
    margin: 2px 0 0 -4px;
    font-size: 25px;
    line-height: 1.2;
  }
  .company-name {
    margin: 34px 0 0 -2px;
    font-size: 29px;
    font-weight: 700;
    line-height: 1.2;
  }
  .company-address {
    margin: 4px 0 0 -2px;
    font-size: 25px;
    line-height: 1.6;
    font-style: normal;
  }
  .contact-list {
    position: absolute;
    right: 45px;
    top: 440px;
    margin: 0;
    padding: 0;
    list-style: none;
    color: var(--ink);
    font-size: 25px;
  }
  .contact-item {
    display: flex;
    justify-content: flex-end;
    align-items: center;
    height: 41px;
  }
  .contact-icon {
    width: 20px;
    height: 20px;
    margin-left: 12px;
    fill: var(--ink);
  }
</style>
</head>
<body>
  <div class="business-card">
    <svg class="card-waves" viewBox="0 0 670 415" preserveAspectRatio="none" aria-hidden="true">
      <path d="M0 226 C 90 175, 230 185, 360 215 C 470 240, 590 240, 670 200 L 670 415 L 0 415 Z" fill="var(--brand-bronze)"/>
      <path d="M0 238 C 110 200, 240 212, 370 245 C 480 272, 600 262, 670 218 L 670 415 L 0 415 Z" fill="var(--brand-yellow)"/>
    </svg>

    <p class="brand-name">Tarvell Homes and Renovations</p>

    <div class="holder-block">
      <h1 class="holder-name">Gus Tarvell</h1>
      <p class="holder-title">President and CEO</p>
      <p class="company-name">Tarvell homes and Renovations</p>
      <address class="company-address">2871 162nd Street Brennick, Northshire<br>T0L3P0</address>
    </div>

    <ul class="contact-list">
      <li class="contact-item">403- 555-0187
        <svg class="contact-icon" viewBox="0 0 24 24" aria-hidden="true"><path d="M6.6 10.8a15 15 0 0 0 6.6 6.6l2.2-2.2a1 1 0 0 1 1-.25 11.4 11.4 0 0 0 3.6.57 1 1 0 0 1 1 1V20a1 1 0 0 1-1 1A17 17 0 0 1 3 4a1 1 0 0 1 1-1h3.5a1 1 0 0 1 1 1c0 1.25.2 2.45.57 3.57a1 1 0 0 1-.25 1z"/></svg>
      </li>
      <li class="contact-item">403- 555-0243
        <svg class="contact-icon" viewBox="0 0 24 24" aria-hidden="true"><path d="M7 1h10a2 2 0 0 1 2 2v18a2 2 0 0 1-2 2H7a2 2 0 0 1-2-2V3a2 2 0 0 1 2-2zm0 3v14h10V4zm5 15.2a1.2 1.2 0 1 0 0 2.4 1.2 1.2 0 0 0 0-2.4z"/></svg>
      </li>
      <li class="contact-item">tarvellhomes@quillmail.example
        <svg class="contact-icon" viewBox="0 0 24 24" aria-hidden="true"><path d="M2 5h20v14H2zm2 2v.5l8 5 8-5V7zm0 2.8V17h16V9.8l-8 5z"/></svg>
      </li>
      <li class="contact-item">tarvellhomes.example
        <svg class="contact-icon" viewBox="0 0 24 24" aria-hidden="true"><path d="M12 2a10 10 0 1 0 0 20 10 10 0 0 0 0-20zm-1 17.9A8 8 0 0 1 4.1 11H7l2 2v2l2 2zm6.9-2.9A2 2 0 0 0 16 15.6h-1v-3a1 1 0 0 0-1-1H8v-2h2a1 1 0 0 0 1-1v-2h2a2 2 0 0 0 2-2v-.4A8 8 0 0 1 17.9 17z"/></svg>
      </li>
    </ul>
  </div>
</body>
</html>
```